Brightwave Audiology Letterhead redesign project

We need a full redesign of our current letterhead to make it consistent with the look and feel of our website design www.brightwaveaudio.com.au. It will need to include all information on the current version attached. The letterhead is used for sending medical reports and general correspondence. It should make use of our corporate colours (purple and teal) as per the logo on the existing file. The letterhead should be bold and eye-catching.

Target Market(s)

Medical practitioners.

Font styles to use
Sans Serif

Requirements
Must have
• It will need to include all information on the current version. Must have a premium, professional, high-end look and feel.
Nice to have
• Bold and eye-catching letterhead that reinforces the Brightwave Audiology brand. To stand out from other traditional letterheads.
Should not have
• The design should not be too cluttered or 'busy'

```html
<!DOCTYPE html>
<html lang="en">
<head>
<meta charset="utf-8">
<title>Brightwave Audiology Letterhead</title>
<link href="https://fonts.googleapis.com/css2?family=Lato:wght@400;700;900&family=Roboto:wght@500;700&display=swap" rel="stylesheet">
<style>
  :root {
    --purple: #7a2d90;
    --teal: #1aae8c;
    --teal-light: #3ccfb0;
    --ink: #3d3d3d;
    --ink-soft: #555;
    --paper: #ffffff;
    --backdrop: #5c5c68;
    --amber: #f3c22d;
  }
  * { box-sizing: border-box; margin: 0; padding: 0; }
  html, body { width: 1200px; height: 992px; overflow: hidden; }
  body { background: var(--backdrop); font-family: "Lato", sans-serif; color: var(--ink); }

  .letterhead {
    position: absolute; left: 245px; top: 16px;
    width: 710px; height: 960px; background: var(--paper);
  }

  .masthead {
    position: absolute; left: 0; top: 0; width: 100%; height: 118px;
    background: var(--purple); color: #fff;
  }
  .brand { position: absolute; left: 56px; top: 34px; }
  .brand-name {
    display: flex; align-items: center; gap: 8px;
    font-family: "Lato", sans-serif; font-weight: 900; font-size: 31px;
    line-height: 1; letter-spacing: -0.5px; color: #fff;
  }
  .brand-dot { width: 14px; height: 14px; border-radius: 50%; background: var(--teal-light); flex: none; }
  .brand-tagline {
    margin-top: 6px; font-family: "Roboto", sans-serif; font-weight: 700;
    font-size: 11px; color: var(--teal-light);
  }

  .contact {
    position: absolute; left: 504px; top: 22px; height: 80px;
    padding-left: 18px; border-left: 1.5px solid var(--teal);
    font-family: "Roboto", sans-serif; font-weight: 500; font-size: 9px; line-height: 13px;
  }
  .contact-address { margin-bottom: 5px; }
  .contact-label { color: var(--teal-light); }
  .contact-line { display: flex; align-items: center; gap: 5px; line-height: 14px; }
  .contact-line svg { width: 8px; height: 8px; flex: none; }

  .letter-body { position: absolute; left: 56px; top: 210px; width: 600px; }
  .date { font-weight: 700; font-size: 13px; }
  .recipient { margin-top: 26px; font-size: 13px; line-height: 17px; }
  .recipient strong { font-weight: 700; }
  .paragraph {
    margin-top: 0; font-size: 12.6px; line-height: 20.9px;
    text-align: justify; color: var(--ink-soft);
  }
  .paragraph + .paragraph { margin-top: 21px; }
  .paragraphs { margin-top: 44px; }

  .signature { margin-top: 62px; }
  .signature-name { font-size: 18px; color: var(--ink); }
  .signature-role { margin-top: 8px; font-size: 12.5px; }

  .footer-credits {
    position: absolute; left: 56px; top: 906px;
    font-family: "Roboto", sans-serif; font-weight: 700; font-size: 7.4px; line-height: 10.5px; color: var(--ink);
  }
  .footer-credits .credits-title { color: var(--teal); }

  .partner-badge { position: absolute; right: 58px; top: 898px; width: 116px; height: 36px; }

  .base-band { position: absolute; left: 0; bottom: 0; width: 100%; height: 14px; background: var(--teal); }
</style>
</head>
<body>
  <main class="letterhead">
    <header class="masthead">
      <div class="brand">
        <div class="brand-name"><span>Brightwave Audiology</span><span class="brand-dot"></span></div>
        <div class="brand-tagline">Independent hearing solutions specialist</div>
      </div>
      <div class="contact">
        <div class="contact-address"><span class="contact-label">CLINIC</span> 48 Alder Street,<br>Ridgeford, Qld 4352</div>
        <div class="contact-line">
          <svg viewBox="0 0 10 10"><path d="M2 1 L4 1 L4.6 3 L3.4 4 Q4.4 6 6 6.6 L7 5.4 L9 6 L9 8 Q9 9 8 9 Q1 8.4 1 2 Q1 1 2 1Z" fill="var(--teal-light)"/></svg>
          07 4100 2233
        </div>
        <div class="contact-line">
          <svg viewBox="0 0 10 10"><rect x="2.5" y="1" width="5" height="3" fill="none" stroke="var(--teal-light)"/><rect x="1" y="4" width="8" height="4" rx="1" fill="var(--teal-light)"/></svg>
          07 4100 2234
        </div>
        <div class="contact-line">
          <svg viewBox="0 0 10 10"><rect x="1" y="2" width="8" height="6" rx="1" fill="var(--teal-light)"/><path d="M1.5 2.5 L5 5.3 L8.5 2.5" fill="none" stroke="var(--purple)" stroke-width="0.9"/></svg>
          hello@brightwaveaudio.com.au
        </div>
        <div class="contact-line">
          <svg viewBox="0 0 10 10"><circle cx="5" cy="5" r="3.8" fill="none" stroke="var(--teal-light)" stroke-width="1.2"/><path d="M1.2 5 H8.8 M5 1.2 Q2.8 5 5 8.8 Q7.2 5 5 1.2" fill="none" stroke="var(--teal-light)" stroke-width="0.8"/></svg>
          www.brightwaveaudio.com.au
        </div>
      </div>
    </header>

    <section class="letter-body">
      <p class="date">February 15, 2018</p>
      <p class="recipient"><strong>Dear Mr. Smith,</strong><br>demo street,<br>demo placeP.O.<br>Box 000, 555 Avenue</p>

      <div class="paragraphs">
        <p class="paragraph">Lorem ipsum dolor sit amet, consectetur adipiscing elit. Donec orci purus, luctus vitae dignissim eu, iaculis sed purus. Vivamus faucibus, ipsum nec aliquet viverra, leo mauris condimentum ligula, sit amet sagittis enim ligula quis arcu. Nam egestas tortor id nisi porttitor mattis. In tortor ante, ultricies in suscipit a, tempus non massa. Vivamus et auctor mi. Fusce vel massa nulla. Phasellus nec eros mauris, et scelerisque orci. Donec malesuada orci vitae nulla accumsan porta a id massa. Quisque accumsan iaculis magna sit amet fringilla. Maecenas consequat, magna eget tincidunt semper, odio nibh rutrum mi, id feugiat ante nisi eu risus. Vestibulum nunc orci, rhoncus a placerat in, ultricies in mi. Cras mattis varius eros, vel fringilla nisi suscipit eget.</p>
        <p class="paragraph">Quisque scelerisque sagittis nulla at porttitor. Mauris a justo et tellus interdum tristique. Sed id augue vitae urna euismod commodo aliquet a quam. Pellentesque arcu velit, cursus et malesuada ut, consequat et diam. Nullam erat sem, rhoncus id ullamcorper vitae, rhoncus et arcu. In ultricies ultricies nulla, ut rutrum nisi iaculis at. Donec eu magna a metus ornare faucibus. Fusce aliquet faucibus ultricies. Morbi semper, est id tincidunt gravida, sem arcu adipiscing lacus, ac bibendum nulla leo eu purus. Quisque nec diam sed risus consectetur a ccumsan quis quis nibh. Vestibulum id purus lorem.</p>
      </div>

      <div class="signature">
        <p class="signature-name">John Doe</p>
        <p class="signature-role">Co-Founder &amp; CEO</p>
      </div>
    </section>

    <footer>
      <div class="footer-credits">
        <div class="credits-title">CLINICAL AUDIOLOGISTS</div>
        <div>DANIEL HARROW BMUS, MAUDST, MAUDSA (CCP)</div>
        <div>SIMON HARROW BN, GRAD DIP FET, MAUDST, MAUDSA (CCP)</div>
      </div>
      <svg class="partner-badge" viewBox="0 0 116 36" role="img" aria-label="Accredited audiologist partner badge">
        <rect x="0" y="2" width="22" height="32" rx="11" fill="var(--amber)" opacity="0.85"/>
        <rect x="28" y="8" width="86" height="1.5" fill="#c8c8c8"/>
        <rect x="28" y="24" width="86" height="1" fill="#d8d8d8"/>
      </svg>
      <div class="base-band"></div>
    </footer>
  </main>
</body>
</html>
```